High end cable company busines card and letterhead

Dear designers,
We assemble high end audio cables that cost a couple of hundred dollars per piece and we are improving the looks of the product.
When people buy a cable they get a leather pouch with the invoice (letterhead) , a business card of the maker and also a quality control card  / warranty card.
The quality control card  is the same size as a business card and the back of the quality control card is the same back as the business card. So we need 4 things:
-1 back of a business card
-1 front of a business card (a file where we can change the name and details of the worker)
-1 quality control front (I will add a photo of an example)
-1 letterhead
We want to make letterpress business cards and use shiny foil for the logo’s. We like the colors black and copper or black and gold for the back. The front of the business card can also be black, copper and white but it does not have to be those colors. We want people to have the feeling that they bought something expensive and high quality.
The front of the quality control card has to be white so we can check things off with a sharpie / pen.
What has to be on the cards:
Business card:
- Our Logo
-Text: Meet the maker (people get the business card of the one who made the cable)
-Name
-Address
-Website (www.talvickwire.com)
-Email address
-Text: For any advise or questions about your cable feel free to contact me.
What has to be on the quality control card:
-Our logo
-Text: quality controll and warranty card (small at the bottom)
-text:
Assembled by:________________
Date: ______-______-____________
QC by:_________________________

Assembly QC [   ]
Measurement QC [   ]
Aesthetics [   ]
(The box [    ] is for the initials of the person that does the QC, it can also be a line or something else)
The letterhead can be your own idea as long as it looks luxurious.
You can download our logo. We have a black one and gold / black but you can change the Color to Match your design. (For instance copper or something) There is also a white one that can be used with the icon on the left.
Some links of stuff we like:
-https://clipvault.example/Rk4wQz81mTa (The looks of this card maybe a bit less busy looking)
-https://b.shopmarrow.com/_qTrvWak
-https://b.shopmarrow.com/_qBu3Lod
-https://b.shopmarrow.com/_qEyaz77

```html
<!DOCTYPE html>
<html lang="en">
<head>
<meta charset="utf-8">
<title>Talvick Wire — Stationery Set</title>
<link rel="stylesheet" href="https://fonts.googleapis.com/css2?family=Outfit:wght@300;400;500;700&display=swap">
<style>
  :root {
    --canvas: #ffffff;
    --paper: #f3f3f3;
    --card-black: #121210;
    --ink: #111111;
    --muted: #7a7a78;
    --muted-dim: #66665f;
    --copper: #a8652a;
    --copper-dark: #5a3414;
    --gold: #c39a2e;
    --rule: #9a9a9a;
    --shadow: 0 3px 6px rgba(0,0,0,0.28);
  }
  * { margin: 0; padding: 0; box-sizing: border-box; }
  html, body { width: 1200px; height: 1200px; overflow: hidden; background: var(--canvas); }
  body { position: relative; font-family: "Outfit", sans-serif; color: var(--ink); }

  .letterhead {
    position: absolute; left: 161px; top: 259px; width: 533px; height: 689px;
    background: var(--paper); box-shadow: var(--shadow);
  }
  .wordmark {
    position: absolute; display: flex; align-items: center; gap: 6px;
    font-family: "Outfit", sans-serif; font-weight: 300; letter-spacing: 0.22em; text-transform: uppercase;
  }
  .wordmark .mark-square { display: inline-block; background: currentColor; }
  .letterhead .wordmark { left: 32px; top: 30px; font-size: 19px; color: var(--ink); }
  .letterhead .wordmark .mark-square { width: 26px; height: 26px; }
  .letterhead-contact {
    position: absolute; left: 33px; top: 566px; font-size: 10px; line-height: 17px;
  }
  .letterhead-contact p { margin-bottom: 17px; }
  .letterhead-contact p:last-child { margin-bottom: 0; }

  .card {
    position: absolute; width: 238px; height: 136px; box-shadow: var(--shadow); overflow: hidden;
  }
  .card::before {
    content: ""; position: absolute; left: 0; top: 0; right: 0; height: 4px;
    background: linear-gradient(90deg, var(--copper-dark), var(--copper) 30%, var(--gold) 55%, var(--copper) 75%, var(--copper-dark));
  }
  .card--dark { background: var(--card-black); color: var(--muted); }
  .card--light { background: #ffffff; color: var(--ink); }
  .card--light::before { background: linear-gradient(90deg, #8a8a88, var(--copper) 25%, var(--gold) 55%, var(--copper) 80%, #9a9a98); }

  .maker-front { left: 541px; top: 328px; }
  .maker-front .wordmark { left: 13px; top: 12px; font-size: 9px; color: var(--muted-dim); gap: 4px; }
  .maker-front .wordmark .mark-square { width: 12px; height: 12px; }
  .maker-front .site { position: absolute; right: 15px; top: 13px; font-size: 7px; }
  .maker-front .contact { position: absolute; left: 13px; top: 70px; font-size: 6.8px; line-height: 8.5px; }
  .maker-front .maker { position: absolute; right: 15px; top: 64px; text-align: right; }
  .maker-front .maker-name { font-size: 12.5px; font-weight: 700; color: var(--muted); line-height: 14px; }
  .maker-front .maker-role { font-size: 5.5px; color: #a0a09c; }
  .maker-front .address { position: absolute; left: 13px; top: 101px; font-size: 6.8px; }
  .maker-front .footnote { position: absolute; left: 13px; top: 123px; font-size: 5px; color: #8f8f8b; }

  .card-back { display: flex; align-items: center; justify-content: center; }
  .card-back .back-name {
    font-size: 15px; font-weight: 400; letter-spacing: 0.3em; color: var(--copper); text-transform: uppercase;
  }
  .card-back-one { left: 541px; top: 501px; height: 135px; }
  .card-back-two { left: 809px; top: 812px; width: 237px; height: 135px; }

  .qc-card { left: 809px; top: 639px; width: 237px; }
  .qc-card .texture {
    position: absolute; left: 0; top: 55px; width: 237px; height: 50px;
    background: linear-gradient(170deg, rgba(255,255,255,0) 20%, rgba(205,205,205,0.45) 55%, rgba(255,255,255,0) 90%);
  }
  .qc-field {
    position: absolute; left: 22px; display: flex; align-items: flex-end; font-size: 7px; font-weight: 500;
  }
  .qc-field .line { border-bottom: 0.6px solid var(--rule); margin-left: auto; height: 1px; }
  .qc-card .qc-title { position: absolute; left: 22px; top: 117px; font-size: 5.8px; font-weight: 500; letter-spacing: 0.02em; }
  .qc-card .wordmark { left: 163px; top: 114px; font-size: 7px; color: var(--ink); gap: 3px; }
  .qc-card .wordmark .mark-square { width: 10px; height: 10px; }
</style>
</head>
<body>

<section class="letterhead" aria-label="Letterhead">
  <div class="wordmark"><span class="mark-square"></span>Talvick Wire</div>
  <div class="letterhead-contact">
    <p>+00 987 654 321</p>
    <p>talvickwire.com</p>
    <p>Talvickwire, Street #48,<br>Block C, State, Country</p>
  </div>
</section>

<section class="card card--dark maker-front" aria-label="Business card front">
  <div class="wordmark"><span class="mark-square"></span>Talvick Wire</div>
  <div class="site">talvickwire.com</div>
  <div class="contact">+00 987 654 321<br>aren.holt@talvickwire.com</div>
  <div class="maker">
    <div class="maker-name">Aren Holt</div>
    <div class="maker-role">Meet the maker *</div>
  </div>
  <div class="address">Talvickwire, Street #48, Block C, State, Country</div>
  <div class="footnote">* For Any Advise Or Questions About Your Cable Feel Free To Contact Me</div>
</section>

<section class="card card--dark card-back card-back-one" aria-label="Business card back">
  <span class="back-name">Talvick</span>
</section>

<section class="card card--light qc-card" aria-label="Quality control card front">
  <div class="texture" role="img" aria-label="Soft grey dotted wave texture"></div>
  <div class="qc-field" style="top:21px;width:194px;">Assembled by:<span class="line" style="width:128px;"></span></div>
  <div class="qc-field" style="top:32px;width:194px;">Date:<span class="line" style="width:154px;"></span></div>
  <div class="qc-field" style="top:43px;width:194px;">QC by:<span class="line" style="width:154px;"></span></div>
  <div class="qc-field" style="top:66px;width:194px;">Assembly QC<span class="line" style="width:128px;"></span></div>
  <div class="qc-field" style="top:77px;width:194px;">Measurement QC<span class="line" style="width:116px;"></span></div>
  <div class="qc-field" style="top:88px;width:194px;">Aesthetics<span class="line" style="width:141px;"></span></div>
  <div class="qc-title">QUALITY CONTROLL &amp; WARRANTY CARD</div>
  <div class="wordmark"><span class="mark-square"></span>Talvick</div>
</section>

<section class="card card--dark card-back card-back-two" aria-label="Quality control card back">
  <span class="back-name">Talvick</span>
</section>

</body>
</html>
```